Needing a business Card for new fire company.

Velm, sales fire equipment and parts. We also do tree clearing for the forest service. My logo will be attached to this. I am also looking for a design that when people see the card it stick with them and they will remember my sales team giving it to them.

```html
<!DOCTYPE html>
<html lang="en">
<head>
<meta charset="utf-8">
<title>Velm Business Card</title>
<link rel="stylesheet" href="https://fonts.googleapis.com/css2?family=Exo+2:wght@400;500;800&display=swap">
<style>
  :root {
    --stage: #e4e4e4;
    --card-white: #ffffff;
    --card-black: #1a1a1a;
    --ink: #111111;
    --ink-soft: #555555;
    --fire-red: #c8202a;
    --divider: #dcdcdc;
    --back-text: #d8d8d8;
  }
  * { box-sizing: border-box; margin: 0; padding: 0; }
  html, body { width: 1200px; height: 960px; overflow: hidden; }
  body {
    background: var(--stage);
    font-family: "Exo 2", Arial, sans-serif;
    position: relative;
  }
  .card {
    position: absolute;
    left: 250px;
    width: 700px;
    height: 400px;
    overflow: hidden;
    box-shadow: 0 6px 18px rgba(0,0,0,0.18);
  }
  /* Back side */
  .card-back { top: 40px; background: var(--card-black); }
  .back-mark {
    position: absolute;
    left: 0; right: 0; top: 130px;
    text-align: center;
    font-weight: 800;
    font-size: 72px;
    color: #3a3a3a;
  }
  .back-url {
    position: absolute;
    left: 0; right: 0; top: 250px;
    text-align: center;
    font-size: 15px;
    letter-spacing: 6px;
    color: var(--back-text);
  }
  /* Front side */
  .card-front { top: 500px; background: var(--card-white); }
  .brand {
    position: absolute;
    left: 70px; top: 150px;
    width: 280px;
    display: flex; align-items: center; justify-content: center; gap: 14px;
  }
  .brand-square { width: 22px; height: 22px; background: var(--fire-red); }
  .brand-name {
    font-weight: 800;
    font-size: 64px;
    color: var(--ink);
    text-transform: uppercase;
    letter-spacing: 2px;
  }
  .divider {
    position: absolute;
    left: 405px; top: 40px;
    width: 1px; height: 250px;
    background: var(--divider);
  }
  .contact { position: absolute; left: 435px; top: 48px; }
  .person-name {
    font-weight: 800; font-size: 21px; color: var(--ink);
    text-transform: uppercase; letter-spacing: 0.5px;
  }
  .person-role { font-size: 15px; color: var(--fire-red); margin-top: 1px; }
  .address { font-size: 15px; color: var(--ink-soft); line-height: 1.3; margin-top: 10px; margin-left: 14px; }
  .channels { list-style: none; margin-top: 12px; }
  .channels li {
    display: flex; align-items: center; gap: 10px;
    font-size: 16px; color: var(--ink-soft); line-height: 1.35;
  }
  .channels svg { width: 12px; height: 12px; fill: var(--fire-red); flex: none; }
  .band-black {
    position: absolute; left: 0; bottom: 0;
    width: 415px; height: 14px; background: var(--card-black);
  }
  .band-red {
    position: absolute; left: 415px; bottom: 0;
    width: 285px; height: 22px; background: var(--fire-red);
  }
</style>
</head>
<body>
  <section class="card card-back" aria-label="Card back">
    <div class="back-mark">Velm</div>
    <div class="back-url">VELM.COM</div>
  </section>

  <section class="card card-front" aria-label="Card front">
    <div class="brand">
      <span class="brand-square"></span>
      <span class="brand-name">Velm</span>
    </div>
    <div class="divider"></div>
    <div class="contact">
      <p class="person-name">Daniel Reyes</p>
      <p class="person-role">President</p>
      <p class="address">4120 Birchwood Road<br>Fairbanks, Alaska 99701</p>
      <ul class="channels">
        <li><svg viewBox="0 0 12 12"><path d="M2 1l2.5 0 1 3-1.5 1a6 6 0 0 0 3 3l1-1.5 3 1V11C5 11 1 7 1 2z"/></svg>555-214-9860</li>
        <li><svg viewBox="0 0 12 12"><path d="M3 0h6a1 1 0 0 1 1 1v10a1 1 0 0 1-1 1H3a1 1 0 0 1-1-1V1a1 1 0 0 1 1-1zm0 2v7h6V2z"/></svg>555-318-5472</li>
        <li><svg viewBox="0 0 12 12"><path d="M3 0h6v4H3zM1 5h10v5H9v2H3v-2H1zm3 3v3h4V8z"/></svg>555-427-3651</li>
        <li><svg viewBox="0 0 12 12"><path d="M0 2h12v8H0zm1 1v.4l5 3.3 5-3.3V3z"/></svg>name@velm.com</li>
        <li><svg viewBox="0 0 12 12"><circle cx="6" cy="6" r="5.5"/></svg>www.velm.com</li>
      </ul>
    </div>
    <div class="band-black"></div>
    <div class="band-red"></div>
  </section>
</body>
</html>
```